Local Newspaper Quarterly " Meet The Realtor" print ad

I need a new add made up. This was my last ad:
http://www.heraldpostlistings.example/static/pdfs/agents1309/Ar092213%20G10%20006%20Prepress.pdf

I do not really care of Realtor advertisements because they are just so cheesy and rather pompous-like. However, it's a necessary evil
My ads have always been outside of the box and/or visually sharp.
I now have a new company' Vorel Real Estate( I will attach a logo) contact info:
Cale Vorel
Vorel Real Estate
Broker/Owner( this can be somewhere in small print or corner of ad since it's mandatory to have shown
Phone: 304-555-0147
Email: Cale@VorelRealEstate.Example
VorelRealEstate.Example
I would like social icons(FB,Twitter, Pinterest! (plain square, no name), Gplus)

Ideas: In my logo font or using the image at the top I envision
Something like:
A
Vorel Real Estate
Of Mind
Body of ad?
Images of Charleston WV as a real light back ground
With 3 or 4 customer reviews chosen by you in this site:
http://webcale.example/think.html

Bottom: contact info and my name in a nice Signature style ??
My agent pic at the bottom right( to be small. I don't want my big head overshadowing the message)

I have yet to think of a tagline for my new company:
I have been thinking of " Luxury Services For All Things Real Estate"

Or nothing at all ??? I don't care for tag lines but then again that's part of the business

Target Market(s)

Higher end homes

Industry/Entity Type

Business

Colors
0f59a5
0392cd
0f0f0f
eaeaea
ffffff

Requirements
Must have
• My logo and colors
Nice to have
• My agent picture and client review.
Should not have
• No typical real estate images like a house or home buyer

```html
<!DOCTYPE html>
<html lang="en">
<head>
<meta charset="utf-8">
<title>Vorel Real Estate – Meet The Realtor</title>
<link rel="stylesheet" href="https://fonts.googleapis.com/css2?family=Archivo:wght@700;800;900&family=Roboto:ital,wght@1,900&family=Roboto+Condensed:wght@400;700&family=Great+Vibes&display=swap">
<style>
  :root{
    --brand-blue:#0f59a5;
    --brand-sky:#0392cd;
    --ink:#0f0f0f;
    --charcoal:#2b2b2b;
    --mist:#eaeaea;
    --white:#ffffff;
    --olive-ink:#2e2e1c;
    --muted:#c9c9c9;
  }
  *{margin:0;padding:0;box-sizing:border-box}
  html,body{width:1200px;height:912px;overflow:hidden;background:var(--white)}
  .ad{position:relative;width:1200px;height:912px;overflow:hidden;background:var(--white)}

  .masthead{position:absolute;left:0;top:0;width:1200px;height:172px;background:var(--brand-blue)}
  .brand-panel{position:absolute;left:0;top:0;width:455px;height:172px;background:var(--charcoal);border-bottom-right-radius:14px;display:flex;align-items:center;justify-content:center;gap:14px}
  .brand-mark{width:26px;height:26px;border-radius:50%;background:var(--brand-sky)}
  .brand-name{font-family:"Archivo",sans-serif;font-weight:800;font-size:34px;color:var(--white);letter-spacing:1px}
  .tagline{position:absolute;left:455px;right:0;top:32px;text-align:center;font-family:"Archivo",sans-serif;font-weight:900;font-size:38px;line-height:57px;color:var(--white);letter-spacing:.3px;text-shadow:1px 2px 3px rgba(0,0,0,.35)}

  .reviews{position:absolute;left:0;top:172px;width:1200px;height:503px}
  .reviews-backdrop{position:absolute;inset:0;background:linear-gradient(180deg,#f4f4f4 0%,#d9d9d9 45%,#e6e6e6 70%,#cfcfcf 100%)}
  .review{position:absolute;left:0;width:1200px;text-align:center;background:rgba(255,255,255,.35);border-bottom:3px solid rgba(170,170,170,.7)}
  .review:last-child{border-bottom:none}
  .review-author{font-family:"Roboto",sans-serif;font-style:italic;font-weight:900;font-size:23px;line-height:28px;color:var(--ink);margin-top:32px;letter-spacing:1px}
  .review-text{font-family:"Roboto Condensed",sans-serif;font-size:25px;line-height:29px;color:var(--ink);margin-top:7px;padding:0 10px}
  .r1{top:0;height:138px}
  .r2{top:138px;height:122px}
  .r2 .review-author{margin-top:16px}
  .r3{top:260px;height:119px}
  .r3 .review-author{margin-top:16px}
  .r4{top:379px;height:124px}
  .r4 .review-author{margin-top:17px}

  .contact{position:absolute;left:0;top:675px;width:737px;height:145px;background:var(--mist)}
  .web{position:absolute;left:26px;top:34px;font-family:"Archivo",sans-serif;font-weight:800;font-size:35px;color:var(--olive-ink)}
  .email{position:absolute;left:56px;top:86px;font-family:"Roboto Condensed",sans-serif;font-size:27px;color:var(--olive-ink);letter-spacing:.5px}
  .social{position:absolute;left:518px;top:28px;width:200px;height:100px}
  .social-tile{position:absolute;width:42px;height:42px;border-radius:8px}
  .t-a{left:26px;top:2px;width:44px;height:60px;border-radius:0;background:#7ac143}
  .t-b{left:106px;top:2px;background:#3b5998}
  .t-c{left:154px;top:2px;border-radius:50%;background:#29a9e1}
  .t-d{left:106px;top:56px;background:#cb2027}
  .t-e{left:154px;top:56px;background:#d34836}

  .phone-bar{position:absolute;left:0;top:820px;width:737px;height:92px;background:var(--brand-blue);display:flex;align-items:center;justify-content:center}
  .phone{font-family:"Archivo",sans-serif;font-weight:800;font-size:64px;color:var(--white);letter-spacing:6px}

  .agent-photo{position:absolute;left:737px;top:675px;width:235px;height:237px;background:linear-gradient(160deg,#8a6a2c 0%,#b88a3a 35%,#c9c6be 65%,#8f8f86 100%)}
  .agent-card{position:absolute;left:972px;top:675px;width:228px;height:237px;background:var(--charcoal);text-align:center;color:var(--white)}
  .signature{position:absolute;left:0;right:0;top:64px;font-family:"Great Vibes",cursive;font-size:42px;color:var(--white);transform:rotate(-12deg)}
  .agent-company{position:absolute;left:0;right:0;top:168px;font-family:"Archivo",sans-serif;font-weight:700;font-size:18px}
  .agent-title{position:absolute;left:0;right:0;top:196px;font-family:"Roboto Condensed",sans-serif;font-size:19px;color:var(--muted)}
</style>
</head>
<body>
<main class="ad">
  <header class="masthead">
    <div class="brand-panel">
      <span class="brand-mark"></span>
      <span class="brand-name">Vorel Real Estate</span>
    </div>
    <h1 class="tagline">LUXURY SERVICES FOR<br>ALL THINGS REAL ESTATE</h1>
  </header>

  <section class="reviews">
    <div class="reviews-backdrop" role="img" aria-label="Faint black and white photograph of a steel arch bridge over a river in Charleston, WV"></div>
    <article class="review r1">
      <p class="review-author">Warren D. Lytle</p>
      <p class="review-text">Cale was fantastic. He knew exactly what I was looking for and found the absolute perfect house for me.<br>Truly an asset to his company!</p>
    </article>
    <article class="review r2">
      <p class="review-author">Marla Pennick</p>
      <p class="review-text">I could not have asked for more support in my home search. I have already recommended Cale to a few people<br>thinking about buying a new home.</p>
    </article>
    <article class="review r3">
      <p class="review-author">Dolores Ashcroft and Janelle Pruitt Huntington,WV</p>
      <p class="review-text">Cale, Thanks for proving me wrong! I told the kids the Milton property would be the toughest to sell. With proper<br>marketing, you moved it fast! Thank you for your hard work. You are the best!</p>
    </article>
    <article class="review r4">
      <p class="review-author">Lorraine Bexley Huntington,WV</p>
      <p class="review-text">Cale is a great asset to your company. I have already given his name to several new Doctors moving to the area<br>that are joining us at Ashfield Valley University physicians.</p>
    </article>
  </section>

  <section class="contact">
    <p class="web">VorelRealEstate.Example</p>
    <p class="email">Cale@VorelRealEstate.Example</p>
    <div class="social" aria-label="Social profiles">
      <span class="social-tile t-a"></span>
      <span class="social-tile t-b"></span>
      <span class="social-tile t-c"></span>
      <span class="social-tile t-d"></span>
      <span class="social-tile t-e"></span>
    </div>
  </section>

  <div class="phone-bar"><p class="phone">304-555-0147</p></div>

  <div class="agent-photo" role="img" aria-label="Portrait photo of the broker in a light shirt, autumn trees behind"></div>
  <aside class="agent-card">
    <p class="signature">Cale Vorel</p>
    <p class="agent-company">VOREL REAL ESTATE</p>
    <p class="agent-title">Broker/Owner</p>
  </aside>
</main>
</body>
</html>
```